Window and GutterCleaning Flyer A5 size double sided.

We need a double sided A5 flyer. Side 1, is for window cleaning, side 2 is for gutter cleaning. Licensed by Borough of Halvern Council.
Phone number 0800 315 4720.
Business address 7 Tarnlow Brae, North Pellin Edinburgh EH14 3RW.
www.clearpane-vista-services.com
We use a LoftPro Gutter inspection Cam to view your gutters first to see if they need doing.
Window cleaning ; Professional window cleaning services, what we offer, water fed pole window cleaning able to reach windows up to 60 feet.
Conservatory cleaning.
Conservatory roof cleaning.
Fascias & Soffits cleaning.
Excellent Customer Service.
Target Market(s)
domestic houses
Industry/Entity Type
window cleaning
Look and feel
Each slider illustrates characteristics of the customer's brand and the style your logo design should communicate.

```html
<!DOCTYPE html>
<html lang="en">
<head>
<meta charset="utf-8">
<title>ClearPane Vista – Window &amp; Gutter Cleaning Flyer</title>
<link rel="stylesheet" href="https://fonts.googleapis.com/css2?family=Bebas+Neue&family=Montserrat:wght@400;800&family=Roboto:ital,wght@0,500;0,700;1,400&display=swap">
<style>
  :root {
    --navy: #2b2961;
    --sky: #9cc8ec;
    --white: #ffffff;
    --paper: #f4f4f6;
    --backdrop: #cbd1e3;
    --brick: #8d5a45;
    --glass: #c9d6df;
  }
  * { margin: 0; padding: 0; box-sizing: border-box; }
  html, body { width: 1200px; height: 933px; overflow: hidden; background: var(--backdrop); }
  .canvas { position: relative; width: 1200px; height: 933px; }

  .flyer {
    position: absolute; top: 135px; width: 469px; height: 663px;
    overflow: hidden; background: var(--navy);
    box-shadow: 0 18px 24px -12px rgba(40, 45, 80, .35);
  }
  .flyer--windows { left: 121px; }
  .flyer--gutters { left: 610px; }

  .hero-photo { position: absolute; left: 0; top: 0; width: 100%; }
  .flyer--windows .hero-photo {
    height: 320px;
    background: linear-gradient(160deg, #a86b52 0%, #c9b3a6 35%, #dfe6ec 60%, #8f6a55 100%);
  }
  .flyer--gutters .hero-photo {
    height: 420px;
    background:
      linear-gradient(180deg, rgba(43,41,97,0) 72%, var(--navy) 100%),
      linear-gradient(170deg, #6f625c 0%, #9a6d5b 25%, #d9cdb0 45%, #8b5145 70%, #6a4d47 100%);
  }

  .brand-block {
    position: absolute; top: 19px; right: 2px; width: 122px; height: 89px;
    background: var(--white);
    display: flex; align-items: center; justify-content: center;
  }
  .brand-name {
    font-family: "Roboto", sans-serif; font-weight: 700; font-size: 17px;
    line-height: 1.1; color: var(--navy); text-align: center;
  }

  .arch { position: absolute; left: 0; top: 260px; width: 469px; height: 160px; }

  .photo-circle {
    position: absolute; border-radius: 50%;
  }
  .camera-shot {
    left: 154px; top: 172px; width: 146px; height: 146px;
    border: 5px solid var(--navy);
    background: radial-gradient(circle at 45% 45%, #3f4a5a 0%, #6f7680 45%, #e98a2e 80%, #e7e7e7 100%);
  }

  .headline {
    position: absolute; left: 0; width: 100%; text-align: center;
    font-family: "Bebas Neue", sans-serif; color: var(--white);
    font-size: 72px; line-height: 1; letter-spacing: -1px;
    transform: scaleY(1.1);
  }
  .flyer--windows .headline { top: 330px; }
  .flyer--gutters .headline { top: 400px; }

  .offer-panel {
    position: absolute; left: 0; top: 413px; width: 100%; height: 194px;
    background: var(--paper);
  }
  .tagline {
    position: absolute; left: 0; top: 6px; width: 100%; text-align: center;
    font-family: "Roboto", sans-serif; font-weight: 700; font-size: 21px;
    color: var(--navy);
  }
  .offer-label {
    position: absolute; left: 19px; top: 40px; width: 187px; height: 28px;
    background: var(--sky); padding-left: 5px;
    font-family: "Montserrat", sans-serif; font-weight: 800; font-size: 15px;
    line-height: 29px; color: var(--navy);
  }
  .offer-list {
    position: absolute; left: 19px; top: 80px; width: 270px;
    list-style: none;
    font-family: "Montserrat", sans-serif; font-size: 13.4px; line-height: 16px;
    color: #1c1c24;
  }
  .offer-list li { position: relative; padding-left: 17px; }
  .offer-list li::before {
    content: ""; position: absolute; left: 1px; top: 7px;
    width: 2px; height: 2px; background: #1c1c24; border-radius: 50%;
  }
  .pole-shot {
    left: 343px; top: 448px; width: 110px; height: 110px;
    border: 4px solid var(--white);
    background: linear-gradient(135deg, #3a4046 0%, #d7dde2 55%, #8c9299 100%);
  }
  .spray-shot {
    left: 284px; top: 493px; width: 96px; height: 96px;
    border: 4px solid var(--white);
    background: linear-gradient(90deg, #6f8fb5 0%, #c8d4e0 45%, #9a5d45 60%, #c59a80 100%);
  }

  .footer {
    position: absolute; left: 0; top: 607px; width: 100%; height: 56px;
    padding-top: 9px; text-align: center;
    font-family: "Roboto", sans-serif; font-style: italic; font-size: 10.6px; line-height: 13.5px;
  }
  .flyer--windows .footer { background: var(--navy); color: var(--white); }
  .flyer--gutters .footer { background: var(--white); color: var(--navy); padding-top: 5px; }

  .cam-callout {
    position: absolute; left: 42px; top: 484px; width: 330px; height: 96px;
    background: var(--sky);
    padding: 20px 0 0 15px;
    font-family: "Roboto", sans-serif; font-weight: 500; font-size: 15.5px; line-height: 19px;
    color: var(--navy);
  }
  .gutter-shot {
    left: 330px; top: 468px; width: 134px; height: 134px;
    border: 4px solid var(--sky);
    background: linear-gradient(150deg, #4d7a3c 0%, #8ea976 40%, #6b6b6f 70%, #b2aaa2 100%);
  }
</style>
</head>
<body>
<div class="canvas">

  <section class="flyer flyer--windows">
    <div class="hero-photo" role="img" aria-label="Photo of a white uPVC conservatory on a red brick house"></div>
    <svg class="arch" viewBox="0 0 469 160" aria-hidden="true">
      <path d="M0 26 Q235 -34 469 30 L469 160 L0 160 Z" fill="#2b2961"/>
    </svg>
    <div class="brand-block"><span class="brand-name">ClearPane<br>Vista</span></div>
    <div class="photo-circle camera-shot" role="img" aria-label="Photo of a handheld inspection camera with screen"></div>
    <h1 class="headline">WINDOW CLEANING</h1>
    <div class="offer-panel">
      <p class="tagline">Professional window cleaning services</p>
      <h2 class="offer-label">WHAT WE OFFER</h2>
      <ul class="offer-list">
        <li>water fed pole window cleaning able to reach windows up to 60 feet.</li>
        <li>Conservatory cleaning.</li>
        <li>Conservatory roof cleaning.</li>
        <li>Fascias &amp; Soffits cleaning.</li>
        <li>Excellent Customer Service.</li>
      </ul>
    </div>
    <div class="photo-circle pole-shot" role="img" aria-label="Photo of a water fed pole brush cleaning a window"></div>
    <div class="photo-circle spray-shot" role="img" aria-label="Photo of a pole brush spraying water beside a house"></div>
    <footer class="footer">
      Licensed by Borough of Halvern Council. Phone number 0800 315 4720.<br>
      Business address 7 Tarnlow Brae, North Pellin Edinburgh EH14 3RW.<br>
      www.clearpane-vista-services.com
    </footer>
  </section>

  <section class="flyer flyer--gutters">
    <div class="hero-photo" role="img" aria-label="Photo of a cleaner in a hi-vis vest using a pole on a conservatory roof"></div>
    <div class="brand-block"><span class="brand-name">ClearPane<br>Vista</span></div>
    <h1 class="headline">GUTTERCLEANING</h1>
    <p class="cam-callout">We use a LoftPro Gutter inspection<br>Cam to view your gutters first to see<br>if they need doing.</p>
    <div class="photo-circle gutter-shot" role="img" aria-label="Photo of a gutter vacuum pole at a roof gutter above a garden"></div>
    <footer class="footer">
      Licensed by Borough of Halvern Council. Phone number 0800 315 4720.<br>
      Business address 7 Tarnlow Brae, North Pellin Edinburgh EH14 3RW.<br>
      www.clearpane-vista-services.com
    </footer>
  </section>

</div>
</body>
</html>
```